Online medical reviews website needs banner advert!

We need banner advert templates for our website, www.traineepanel.net. These should meet the technical requirements of our partner (uploaded).

Our groundbreaking website allows doctors in training to rate and review their training.

The adverts should use the same modern design language and colour scheme as our website. They should use the text 'Help a junior doctor make a big decision - rate your training!'.

Vector assets should be supplied, allowing us to use alternative text in future.
Updates

Industry/Entity Type

Healthcare

Font styles to use
Other font styles liked:
• Karla

Colors
3277b5
0555a3
ffffff

Requirements
Must have
• Similar design to our website. Should be elegant & modern. Must allow future text to be easily inserted.
Should not have
• Unrelated design.

```html
<!DOCTYPE html>
<html lang="en">
<head>
<meta charset="UTF-8">
<title>Trainee Panel – Banner</title>
<link href="https://fonts.googleapis.com/css2?family=Karla:wght@400;700;800&display=swap" rel="stylesheet">
<style>
  :root {
    --navy: #03257c;
    --button-blue: #2c4f9c;
    --white: #ffffff;
    --photo-light: #f1f6fb;
    --photo-mid: #d6e6f2;
    --photo-deep: #9fc6e0;
  }
  * { margin: 0; padding: 0; box-sizing: border-box; }
  html, body {
    width: 1200px;
    height: 451px;
    overflow: hidden;
    background: var(--white);
  }
  .banner {
    position: relative;
    width: 1200px;
    height: 451px;
    background: var(--navy);
    font-family: "Karla", Arial, sans-serif;
    color: var(--white);
    overflow: hidden;
  }
  .banner__photo {
    position: absolute;
    inset: 0;
    width: 1200px;
    height: 451px;
  }
  .brand {
    position: absolute;
    top: 22px;
    right: 44px;
    font-size: 24px;
    font-weight: 400;
    letter-spacing: -0.3px;
    color: var(--white);
  }
  .headline {
    position: absolute;
    left: 540px;
    width: 636px;
    top: 112px;
    text-align: center;
    font-size: 36px;
    font-weight: 800;
    line-height: 50px;
    letter-spacing: 1px;
  }
  .cta {
    position: absolute;
    left: 771px;
    top: 262px;
    width: 182px;
    height: 27px;
    background: var(--button-blue);
    display: flex;
    align-items: center;
    justify-content: center;
    font-size: 11.5px;
    font-weight: 700;
    letter-spacing: 0.2px;
  }
  .site-url {
    position: absolute;
    left: 700px;
    width: 316px;
    top: 410px;
    text-align: center;
    font-size: 11.5px;
    font-weight: 700;
    letter-spacing: 2.4px;
  }
</style>
</head>
<body>
  <div class="banner">
    <svg class="banner__photo" viewBox="0 0 1200 451" role="img" aria-label="Photo of a surgical team operating on a patient in a bright theatre with lamps and an anaesthesia cart, washed in pale blue">
      <defs>
        <linearGradient id="theatre-wash" x1="0" y1="0" x2="0.6" y2="1">
          <stop offset="0" stop-color="var(--photo-mid)"/>
          <stop offset="0.4" stop-color="var(--photo-light)"/>
          <stop offset="0.75" stop-color="var(--photo-mid)"/>
          <stop offset="1" stop-color="var(--photo-deep)"/>
        </linearGradient>
      </defs>
      <polygon points="0,0 458,0 524,236 640,300 688,451 0,451" fill="url(#theatre-wash)"/>
    </svg>

    <div class="brand">Trainee Panel</div>

    <h1 class="headline">Help a junior doctor make a big decision</h1>

    <div class="cta">Rate &amp; review your training!</div>

    <div class="site-url">www.traineepanel.net</div>
  </div>
</body>
</html>
```